WooCommerce Web Design for SEO Agency

Looking for a clean and fast WooCommerce design

Selling 5 different products each with maybe 3-4 variants

Need imagery - featured images, basic logo etc

I will supply all content and most is ready to go (or can be in a few days)

You will need to design and build the site including some basic WooCommerce configuration - PayPal, checkout forms etc

Target Market(s)

SEO, Internet marketers

Coding

Coded - Design and coding required

Number of Pages Required

3 page

Font styles to use
Sans Serif

Requirements
Must have
• WooCommerce and WP integration

```html
<!DOCTYPE html>
<html lang="en">
<head>
<meta charset="utf-8">
<title>RankWell – Website Content</title>
<link href="https://fonts.googleapis.com/css2?family=Open+Sans:wght@400;600;700&display=swap" rel="stylesheet">
<style>
:root{
  --blue:#1f6fc5;
  --blue-dark:#16589f;
  --navy:#0d2d52;
  --navy-deep:#08203c;
  --text:#555b63;
  --muted:#8c9299;
  --line:#e3e6ea;
  --soft:#f4f6f8;
  --grey-head:#8e9297;
  --white:#ffffff;
}
*{box-sizing:border-box;margin:0;padding:0}
html,body{width:1200px;height:3084px;overflow:hidden}
body{font-family:'Open Sans',Arial,sans-serif;color:var(--text);background:var(--white);font-size:14px;line-height:1.6}
.topbar{height:36px;background:var(--navy);color:#cfd9e6;font-size:12px;display:flex;justify-content:flex-end;align-items:center;gap:28px;padding:0 110px}
.topbar span{display:flex;align-items:center;gap:6px}
.nav{height:74px;display:flex;align-items:center;justify-content:space-between;padding:0 110px;border-bottom:1px solid var(--line)}
.brand{display:flex;align-items:center;gap:10px;font-weight:700;font-size:24px;color:var(--blue)}
.brand i{width:26px;height:26px;border-radius:50%;background:var(--blue);display:block}
.menu{display:flex;gap:34px;font-size:13px;font-weight:600;color:#4a4f55;align-items:center}
.menu .active{color:var(--blue)}
.hero{height:130px;background:linear-gradient(100deg,#2b5f97,#4f86bf 50%,#2c5a8c);display:flex;align-items:center;justify-content:center}
.hero h1{color:var(--white);font-size:30px;font-weight:600}
.intro{height:260px;display:flex;align-items:center;justify-content:center;gap:50px;padding:0 160px}
.intro-media{width:420px;height:190px;background:linear-gradient(135deg,#dfe9f4,#b9cde3);border-radius:2px;flex:none}
.intro-copy p{font-size:13px;margin-bottom:18px}
.btn{display:inline-block;padding:7px 22px;border-radius:16px;font-size:12px;font-weight:600;background:#6f757c;color:var(--white)}
.btn-blue{background:var(--blue)}
.btn-outline{background:transparent;border:1px solid #b5bac0;color:#6f757c}
.section-title{text-align:center;font-size:22px;font-weight:600;color:#3d4248}
.section-title em{font-style:normal;color:var(--blue)}
.divider{display:flex;justify-content:center;align-items:center;gap:10px;margin:10px 0 24px}
.divider::before,.divider::after{content:"";width:40px;height:1px;background:#c9cdd2}
.categories{height:400px;padding-top:60px;border-top:1px solid var(--line)}
.cat-grid{display:flex;justify-content:center;gap:160px;margin-top:20px}
.cat{width:320px;text-align:center}
.cat svg{margin-bottom:12px}
.cat h3{color:var(--blue);font-size:17px;font-weight:600;margin-bottom:6px}
.cat p{font-size:12px;color:var(--muted);margin-bottom:18px}
.products{height:580px;background:var(--soft);padding-top:34px}
.label{display:flex;justify-content:center;align-items:center;gap:12px;font-size:11px;color:var(--blue);font-weight:600;margin-bottom:18px}
.label::before,.label::after{content:"";width:320px;height:1px;background:#d8dce1}
.cards{display:flex;justify-content:center;gap:24px;margin-bottom:40px}
.card{width:300px;height:180px;background:var(--white);border:1px solid var(--line);text-align:center;padding-top:26px}
.card h4{font-size:13px;color:var(--blue);font-weight:600;margin:10px 24px 6px;line-height:1.4}
.card .price{font-size:13px;color:#4a4f55}
.packages{height:400px;padding-top:30px;position:relative}
.plans{display:flex;justify-content:center;align-items:flex-start;margin-top:6px}
.plan{width:290px;background:var(--white);border:1px solid var(--line);text-align:center;padding-bottom:20px;margin-top:20px}
.plan-head{background:var(--grey-head);color:var(--white);font-weight:600;font-size:15px;height:64px;display:flex;align-items:center;justify-content:center}
.plan-featured{width:300px;margin-top:0;box-shadow:0 6px 22px rgba(0,0,0,.15);position:relative;overflow:hidden;z-index:1}
.plan-featured .plan-head{background:var(--blue);height:84px}
.ribbon{position:absolute;top:14px;right:-30px;width:110px;height:18px;background:#36b36a;transform:rotate(45deg)}
.price-ring{width:92px;height:92px;border-radius:50%;border:1px solid var(--line);margin:-30px auto 10px;background:var(--white);display:flex;flex-direction:column;align-items:center;justify-content:center;color:#3d4248}
.price-ring b{font-size:30px;font-weight:600;line-height:1}
.price-ring b sup{font-size:14px}
.price-ring small{font-size:10px;color:var(--muted)}
.features{list-style:none;font-size:11px;color:var(--muted);margin:0 50px 14px;text-align:left}
.features li{display:flex;align-items:center;gap:8px;padding:4px 0;border-bottom:1px solid #f0f1f3}
.why{height:540px;border-top:6px solid var(--navy);padding-top:54px}
.why .lead{text-align:center;font-size:12px;color:var(--muted);margin-top:-8px;margin-bottom:32px}
.why-grid{display:grid;grid-template-columns:repeat(3,250px);gap:40px 90px;justify-content:center}
.why-item h4{font-size:15px;color:var(--blue);font-weight:600;margin:8px 0 4px}
.why-item p{font-size:12px;color:var(--muted);line-height:1.5}
.contact{height:520px;background:linear-gradient(135deg,#12406f,#0d2d52);position:relative;padding:34px 110px 0;color:var(--white)}
.contact h2{font-size:20px;font-weight:600;margin-bottom:4px}
.contact .sub{font-size:12px;color:#b8c6d8;margin-bottom:20px}
.form{width:560px;display:grid;grid-template-columns:1fr 1fr;gap:12px}
.field{height:34px;background:var(--white);border-radius:2px}
.field.wide{grid-column:span 2;height:90px}
.send{grid-column:span 2;width:110px;height:32px;background:#6f757c;border-radius:16px;color:var(--white);font-size:12px;font-weight:600;display:flex;align-items:center;justify-content:center}
.portrait{position:absolute;right:110px;bottom:110px;width:300px;height:380px;background:linear-gradient(180deg,#2b5f8f,#1b3f66)}
.info{position:absolute;left:110px;right:110px;bottom:30px;display:flex;gap:90px;font-size:12px;color:#cbd6e4;border-top:1px solid rgba(255,255,255,.15);padding-top:22px}
.info span{display:flex;align-items:center;gap:10px}
.info i{width:30px;height:30px;border-radius:50%;background:var(--blue);display:flex;align-items:center;justify-content:center}
.footer{height:144px;background:var(--navy-deep);display:flex;flex-direction:column;align-items:center;justify-content:center;gap:12px;color:#8da0b8;font-size:11px}
.social{display:flex;gap:10px}
.social i{width:26px;height:26px;border-radius:50%;background:var(--blue);display:block}
.links{display:flex;gap:26px;color:#c5d1df}
</style>
</head>
<body>
<header>
  <div class="topbar">
    <span><svg width="13" height="10" viewBox="0 0 13 10"><rect x=".5" y=".5" width="12" height="9" fill="none" stroke="#cfd9e6"/><path d="M.5 .5l6 5 6-5" fill="none" stroke="#cfd9e6"/></svg>hello@rankwell.example</span>
    <span><svg width="11" height="11" viewBox="0 0 11 11"><path d="M2 1l2 2-1 1.5a6 6 0 0 0 3.5 3.5L8 7l2 2-1.5 1.5C5 10 1 6 .5 2.5z" fill="#cfd9e6"/></svg>+1 555 014 2290</span>
  </div>
  <nav class="nav">
    <div class="brand"><i></i>RankWell</div>
    <div class="menu"><span class="active">Home</span><span>About</span><span>Products ▾</span><span>Contact</span>
      <svg width="16" height="14" viewBox="0 0 16 14"><path d="M1 1h2l2 8h8l2-6H4" fill="none" stroke="#4a4f55" stroke-width="1.4"/><circle cx="6" cy="12" r="1.2" fill="#4a4f55"/><circle cx="12" cy="12" r="1.2" fill="#4a4f55"/></svg></div>
  </nav>
</header>

<section class="hero" role="img" aria-label="Banner photo of a desk with laptop in blue tones"><h1>Website Content</h1></section>

<section class="intro">
  <div class="intro-media" role="img" aria-label="Illustration of content pages and writing tools"></div>
  <div class="intro-copy">
    <p>We write clear, search friendly content for your website that helps pages rank and turns visitors into buyers. Every piece is researched, written by hand and checked before delivery so it is ready to publish. Choose a single page or a monthly plan and we handle the rest.</p>
    <span class="btn">Read More</span>
  </div>
</section>

<section class="categories">
  <h2 class="section-title">Website Content <em>Categories</em></h2>
  <div class="divider"><svg width="12" height="12" viewBox="0 0 12 12"><path d="M2 10l6-6 2 2-6 6H2z" fill="#9aa0a6"/></svg></div>
  <div class="cat-grid">
    <div class="cat">
      <svg width="40" height="40" viewBox="0 0 40 40"><rect x="8" y="4" width="24" height="32" fill="none" stroke="#7d838a" stroke-width="2"/><path d="M13 13h14M13 19h14M13 25h10" stroke="#7d838a" stroke-width="2"/></svg>
      <h3>Category / Landing Page Content</h3>
      <p>Focused copy for category and landing pages that ranks well and sells.</p>
      <span class="btn">View Products</span>
    </div>
    <div class="cat">
      <svg width="40" height="40" viewBox="0 0 40 40"><rect x="4" y="8" width="32" height="24" fill="none" stroke="#7d838a" stroke-width="2"/><path d="M10 16h20M10 22h14" stroke="#7d838a" stroke-width="2"/></svg>
      <h3>Guest Blog Post Content</h3>
      <p>Well written guest posts that earn links and build your authority.</p>
      <span class="btn">View Products</span>
    </div>
  </div>
</section>

<section class="products">
  <div class="label">Category / Landing Page Content</div>
  <div class="cards">
    <div class="card"><svg width="34" height="34" viewBox="0 0 34 34"><rect x="7" y="3" width="20" height="28" fill="none" stroke="#7d838a" stroke-width="2"/><path d="M11 11h12M11 16h12M11 21h8" stroke="#7d838a" stroke-width="2"/></svg><h4>Category / Landing Page Content – 1000 Words</h4><div class="price">£179.00</div></div>
    <div class="card"><svg width="34" height="34" viewBox="0 0 34 34"><rect x="7" y="3" width="20" height="28" fill="none" stroke="#7d838a" stroke-width="2"/><path d="M11 11h12M11 16h12M11 21h8" stroke="#7d838a" stroke-width="2"/></svg><h4>Category / Landing Page Content – 2000 Words</h4><div class="price">£309.00</div></div>
    <div class="card"><svg width="34" height="34" viewBox="0 0 34 34"><rect x="7" y="3" width="20" height="28" fill="none" stroke="#7d838a" stroke-width="2"/><path d="M11 11h12M11 16h12M11 21h8" stroke="#7d838a" stroke-width="2"/></svg><h4>Category / Landing Page Content – 750 Words</h4><div class="price">£149.00</div></div>
  </div>
  <div class="label">Guest Blog Posts</div>
  <div class="cards">
    <div class="card"><svg width="34" height="34" viewBox="0 0 34 34"><rect x="3" y="7" width="28" height="20" fill="none" stroke="#7d838a" stroke-width="2"/><path d="M8 13h18M8 19h12" stroke="#7d838a" stroke-width="2"/></svg><h4>Guest Blog Post Content – 500 Words</h4><div class="price">£49.00</div></div>
    <div class="card"><svg width="34" height="34" viewBox="0 0 34 34"><rect x="3" y="7" width="28" height="20" fill="none" stroke="#7d838a" stroke-width="2"/><path d="M8 13h18M8 19h12" stroke="#7d838a" stroke-width="2"/></svg><h4>Guest Blog Post Content – 1000 Words</h4><div class="price">£89.00</div></div>
    <div class="card"><svg width="34" height="34" viewBox="0 0 34 34"><rect x="3" y="7" width="28" height="20" fill="none" stroke="#7d838a" stroke-width="2"/><path d="M8 13h18M8 19h12" stroke="#7d838a" stroke-width="2"/></svg><h4>Guest Blog Post Content – 1500 Words</h4><div class="price">£129.00</div></div>
  </div>
</section>

<section class="packages">
  <h2 class="section-title">Monthly <em>Packages</em></h2>
  <div class="divider"><svg width="12" height="12" viewBox="0 0 12 12"><path d="M2 10l6-6 2 2-6 6H2z" fill="#9aa0a6"/></svg></div>
  <div class="plans">
    <div class="plan">
      <div class="plan-head">Silver Package</div>
      <div class="price-ring"><b><sup>$</sup>39</b><small>/monthly</small></div>
      <ul class="features"><li>✓ 4 blog posts</li><li>✓ 1 landing page</li><li>✓ Keyword research</li><li>✓ Email support</li></ul>
      <span class="btn btn-outline">Select Package</span>
    </div>
    <div class="plan plan-featured">
      <i class="ribbon"></i>
      <div class="plan-head">Gold Package</div>
      <div class="price-ring"><b><sup>$</sup>59</b><small>/monthly</small></div>
      <ul class="features"><li>✓ 8 blog posts</li><li>✓ 2 landing pages</li><li>✓ Keyword research</li><li>✓ Priority support</li><li>✓ Monthly report</li></ul>
      <span class="btn btn-blue">Select Package</span>
    </div>
    <div class="plan">
      <div class="plan-head">Platinum Package</div>
      <div class="price-ring"><b><sup>$</sup>89</b><small>/monthly</small></div>
      <ul class="features"><li>✓ 12 blog posts</li><li>✓ 4 landing pages</li><li>✓ Full content plan</li><li>✓ Phone support</li></ul>
      <span class="btn btn-outline">Select Package</span>
    </div>
  </div>
</section>

<section class="why">
  <h2 class="section-title">Why <em>Choose Us</em></h2>
  <div class="divider"><svg width="12" height="12" viewBox="0 0 12 12"><path d="M2 10l6-6 2 2-6 6H2z" fill="#9aa0a6"/></svg></div>
  <p class="lead">We help brands grow with honest work, fair prices and content that gets results.</p>
  <div class="why-grid">
    <div class="why-item"><svg width="26" height="26" viewBox="0 0 26 26"><path d="M13 2l9 4v6c0 6-4 10-9 12-5-2-9-6-9-12V6z" fill="none" stroke="#7d838a" stroke-width="2"/></svg><h4>Trust</h4><p>Clients return to us year after year because we deliver what we promise.</p></div>
    <div class="why-item"><svg width="26" height="26" viewBox="0 0 26 26"><path d="M13 2l3 7 7 .5-5.5 4.5 2 7L13 17l-6.5 4 2-7L3 9.5 10 9z" fill="none" stroke="#7d838a" stroke-width="2"/></svg><h4>Experience</h4><p>Over ten years writing for search across many markets and niches.</p></div>
    <div class="why-item"><svg width="26" height="26" viewBox="0 0 26 26"><circle cx="13" cy="9" r="5" fill="none" stroke="#7d838a" stroke-width="2"/><path d="M4 24c1-6 5-8 9-8s8 2 9 8" fill="none" stroke="#7d838a" stroke-width="2"/></svg><h4>Customer Rates</h4><p>Simple, fair pricing with discounts for regular monthly clients.</p></div>
    <div class="why-item"><svg width="26" height="26" viewBox="0 0 26 26"><circle cx="13" cy="13" r="10" fill="none" stroke="#7d838a" stroke-width="2"/><path d="M8 13l4 4 6-8" fill="none" stroke="#7d838a" stroke-width="2"/></svg><h4>Money Back Guarantee</h4><p>If the work is not right we will fix it or refund your order in full.</p></div>
    <div class="why-item"><svg width="26" height="26" viewBox="0 0 26 26"><rect x="3" y="8" width="20" height="14" fill="none" stroke="#7d838a" stroke-width="2"/><path d="M9 8V4h8v4" fill="none" stroke="#7d838a" stroke-width="2"/></svg><h4>Professional Expertise</h4><p>Skilled writers who understand search, structure and your readers.</p></div>
    <div class="why-item"><svg width="26" height="26" viewBox="0 0 26 26"><rect x="5" y="11" width="16" height="12" fill="none" stroke="#7d838a" stroke-width="2"/><path d="M8 11V7a5 5 0 0 1 10 0v4" fill="none" stroke="#7d838a" stroke-width="2"/></svg><h4>Privacy &amp; Confidentiality</h4><p>Your projects and details stay private and are never shared with others.</p></div>
  </div>
</section>

<section class="contact">
  <h2>Contact Me</h2>
  <p class="sub">Send a short note and we will reply within one day.</p>
  <div class="form">
    <div class="field"></div><div class="field"></div>
    <div class="field"></div><div class="field"></div>
    <div class="field wide"></div>
    <div class="send">Send</div>
  </div>
  <div class="portrait" role="img" aria-label="Photo of the agency founder standing"></div>
  <div class="info">
    <span><i><svg width="12" height="14" viewBox="0 0 12 14"><path d="M6 13S1 8 1 5a5 5 0 0 1 10 0c0 3-5 8-5 8z" fill="#fff"/></svg></i>12 Harbour Road, Westfield</span>
    <span><i><svg width="12" height="12" viewBox="0 0 11 11"><path d="M2 1l2 2-1 1.5a6 6 0 0 0 3.5 3.5L8 7l2 2-1.5 1.5C5 10 1 6 .5 2.5z" fill="#fff"/></svg></i>+1 555 014 2290</span>
    <span><i><svg width="13" height="10" viewBox="0 0 13 10"><rect x=".5" y=".5" width="12" height="9" fill="#fff"/><path d="M.5 .5l6 5 6-5" fill="none" stroke="#1f6fc5"/></svg></i>hello@rankwell.example</span>
  </div>
</section>

<footer class="footer">
  <div class="social"><i></i><i></i><i></i></div>
  <div class="links"><span>Home</span><span>Terms</span><span>Contact</span></div>
  <div>© 2024 RankWell. All Rights Reserved.</div>
</footer>
</body>
</html>
```